Business card design needed

Double sided
Color, unique, elegant

Maybe put this quote somewhere?? But I think it might make it to cluttered?
“The Pilates Method of Body
Conditioning develops the body
uniformly, corrects posture, restores
vitality, invigorates the mind and
elevates the spirit”
- Henrik Dovacombe

Industry/Entity Type

Business

Contact Information for Business Card

Marta Kellbrook
Pilates Instructor & Personal trainer
Mobile: 0498265043
www.lorvix.com.au
email: lorvixhealth.fitness@qentamail.com

```html
<!DOCTYPE html>
<html lang="en">
<head>
<meta charset="utf-8">
<title>Lorvix Health and Fitness – Business Card</title>
<link rel="stylesheet" href="https://fonts.googleapis.com/css2?family=Arimo:ital,wght@0,400;0,700;1,400;1,700&display=swap">
<style>
  :root {
    --bg: #ece9e4;
    --green-light: #8fd21e;
    --green-mid: #4fae12;
    --green-deep: #0a6a0c;
    --green-darkest: #045a08;
    --white: #ffffff;
    --ink: #1b2a10;
    --soft-white: rgba(255,255,255,0.92);
  }
  * { margin: 0; padding: 0; box-sizing: border-box; }
  html, body { width: 1200px; height: 1000px; overflow: hidden; }
  body {
    background: var(--bg);
    font-family: "Arimo", Arial, sans-serif;
    position: relative;
  }
  .card {
    position: absolute;
    width: 500px;
    height: 285px;
    overflow: hidden;
    box-shadow: 0 4px 10px rgba(0,0,0,0.35);
  }
  .card--front {
    left: 70px; top: 365px;
    background:
      radial-gradient(ellipse 200px 160px at 70px 120px, rgba(200,245,120,0.75), rgba(200,245,120,0) 70%),
      linear-gradient(90deg, var(--green-mid) 0%, var(--green-light) 18%, var(--green-mid) 45%, var(--green-deep) 70%, var(--green-darkest) 100%);
  }
  .card--back {
    left: 622px; top: 368px;
    background:
      radial-gradient(ellipse 180px 150px at 480px 60px, rgba(210,250,140,0.8), rgba(210,250,140,0) 70%),
      linear-gradient(90deg, var(--green-darkest) 0%, var(--green-deep) 30%, var(--green-mid) 62%, var(--green-light) 100%);
  }

  /* front */
  .quote {
    position: absolute;
    left: 20px; top: 154px;
    width: 170px;
    color: var(--white);
    font-size: 9.3px;
    font-weight: 700;
    font-style: italic;
    line-height: 18.5px;
    text-shadow: 0 1px 2px rgba(0,0,0,0.35);
  }
  .quote__author {
    position: absolute;
    left: 72px; top: 242px;
    color: var(--white);
    font-size: 11px;
    font-style: italic;
    letter-spacing: 0.5px;
  }
  .brand {
    position: absolute;
    color: var(--ink);
    text-align: center;
  }
  .brand__name {
    display: flex; align-items: center; justify-content: center; gap: 8px;
    font-weight: 400;
    letter-spacing: 2px;
  }
  .brand__dot {
    border-radius: 50%;
    background: #c77ac4;
  }
  .brand--front { left: 182px; top: 168px; width: 140px; }
  .brand--front .brand__name { font-size: 34px; }
  .brand--front .brand__dot { width: 14px; height: 14px; }
  .brand--front .brand__tag { font-size: 13px; margin-top: 2px; }

  .ornament {
    position: absolute;
    top: 0; height: 100%;
  }
  .ornament--front {
    right: 0; width: 175px;
    background: linear-gradient(180deg, rgba(255,255,255,0.06), rgba(255,255,255,0.22));
  }
  .ornament--back {
    left: 0; width: 180px;
    background: linear-gradient(180deg, rgba(255,255,255,0.06), rgba(255,255,255,0.22));
  }

  /* back */
  .brand--back { right: 24px; top: 80px; width: 100px; }
  .brand--back .brand__name { font-size: 20px; letter-spacing: 1px; gap: 5px; }
  .brand--back .brand__dot { width: 8px; height: 8px; }
  .brand--back .brand__tag { font-size: 8px; }

  .person {
    position: absolute;
    right: 67px; top: 136px;
    text-align: right;
    color: var(--white);
  }
  .person__name { font-size: 20px; line-height: 24px; }
  .person__role { font-size: 10.5px; color: var(--soft-white); }

  .contacts {
    position: absolute;
    right: 58px; top: 192px;
    list-style: none;
    text-align: right;
    color: var(--white);
    font-size: 12px;
    font-weight: 700;
  }
  .contacts li { height: 25.5px; line-height: 18px; }

  .icon-tab {
    position: absolute;
    right: 0; top: 188px;
    width: 37px; height: 78px;
    background: var(--white);
    border-radius: 4px 0 0 4px;
    display: flex; flex-direction: column; align-items: center; justify-content: space-around;
    padding: 5px 0;
  }
  .icon-tab svg { width: 15px; height: 15px; }
</style>
</head>
<body>

  <section class="card card--front" aria-label="Business card front">
    <p class="quote">“The Pilates Method of Body Conditioning develops the body uniformly, corrects posture, restores vitality, invigorates the mind and elevates the spirit”</p>
    <p class="quote__author">Henrik Dovacombe</p>

    <div class="brand brand--front">
      <div class="brand__name"><span class="brand__dot"></span><span>Lorvix</span></div>
      <div class="brand__tag">Health and Fitness</div>
    </div>

    <div class="ornament ornament--front" role="img" aria-label="White floral swirl ornament with butterflies and stars"></div>
  </section>

  <section class="card card--back" aria-label="Business card back">
    <div class="ornament ornament--back" role="img" aria-label="White floral swirl ornament with butterflies and stars"></div>

    <div class="brand brand--back">
      <div class="brand__name"><span class="brand__dot"></span><span>Lorvix</span></div>
      <div class="brand__tag">Health and Fitness</div>
    </div>

    <div class="person">
      <p class="person__name">Marta Kellbrook</p>
      <p class="person__role">Pilates Instructor &amp; Personal trainer</p>
    </div>

    <ul class="contacts">
      <li>lorvixhealth.fitness@qentamail.com</li>
      <li>www.lorvix.com.au</li>
      <li>0498 265 043</li>
    </ul>

    <div class="icon-tab">
      <svg viewBox="0 0 16 16" aria-label="Email" role="img">
        <rect x="1" y="3" width="14" height="10" fill="none" stroke="#1b2a10" stroke-width="1.3"/>
        <path d="M1 3 L8 9 L15 3 M1 13 L6 7.5 M15 13 L10 7.5" fill="none" stroke="#1b2a10" stroke-width="1.1"/>
      </svg>
      <svg viewBox="0 0 16 16" aria-label="Website" role="img">
        <circle cx="8" cy="8" r="6.5" fill="none" stroke="#1b2a10" stroke-width="1.3"/>
        <ellipse cx="8" cy="8" rx="3" ry="6.5" fill="none" stroke="#1b2a10" stroke-width="1.1"/>
        <path d="M1.5 8 H14.5 M2.5 4.8 H13.5 M2.5 11.2 H13.5" stroke="#1b2a10" stroke-width="1.1"/>
      </svg>
      <svg viewBox="0 0 16 16" aria-label="Phone" role="img">
        <path d="M4 1.5 L6.3 4.5 L4.8 6.2 C5.6 8 7.8 10.4 9.8 11.2 L11.5 9.7 L14.5 12 L12.6 14.3 C8 14 2 8 1.7 3.4 Z" fill="none" stroke="#1b2a10" stroke-width="1.2" stroke-linejoin="round"/>
      </svg>
    </div>
  </section>

</body>
</html>
```